App Design for quiz app (casual gaming app)

We need an design & logo for our quiz app. Its a simple quiz app, where you pick up a category, answer three questions out of this category. After this an opponent is assigned to your game, and has to answer the same three questions. After this first round is finished, it's the opponents turn to choose a new category and answer three questions out of this category. Now it's your turn to answer the same three questions. With this done, the 2nd round is finished. One game has seven rounds.
Please find attached the balsamiq project. For all of you, do not have balsamiq, please find also the mockups as pdf.
Final delivery should be psd files
Target Market(s)
Casual Games

```html
<!DOCTYPE html>
<html lang="en">
<head>
<meta charset="utf-8">
<title>Quiz App – Side Menu</title>
<link rel="stylesheet" href="https://fonts.googleapis.com/css2?family=Source+Sans+3:wght@600&display=swap">
<style>
  :root {
    --status-bar: #000000;
    --base: #ffffff;
    --icon-stroke: #cfc8de;
    --label: #ffffff;
    --row1: #2e2650; --row1-icon: #25214a;
    --row2: #33244f; --row2-icon: #2d2650;
    --row3: #3b2160; --row3-icon: #33264f;
    --row4: #3e2168; --row4-icon: #3a2260;
    --row5: #4e1c6c; --row5-icon: #40236a;
    --row6: #561b74; --row6-icon: #4e1c6c;
    --strip1: #4a1868; --strip2: #461a62; --strip3: #421a5e;
    --strip4: #381c55; --strip5: #321c4e; --strip6a: #2b1c47; --strip6b: #221d40;
    --toggle-bg: #2a2150;
  }
  * { margin: 0; padding: 0; box-sizing: border-box; }
  html, body { width: 1200px; height: 2166px; overflow: hidden; background: var(--base); }
  .screen { position: relative; width: 1200px; height: 2166px; background: var(--base); overflow: hidden; }
  .status-bar { position: absolute; left: 0; top: 0; width: 1200px; height: 98px; background: var(--status-bar); }

  .content-strip { position: absolute; left: 960px; top: 98px; width: 240px; height: 2045px; }
  .content-strip div { position: absolute; left: 0; width: 100%; }

  .side-menu {
    position: absolute; left: 0; top: 98px; width: 960px; height: 2045px;
    box-shadow: 6px 0 14px rgba(0,0,0,0.35); list-style: none;
  }
  .menu-item { position: absolute; left: 0; width: 960px; display: flex; align-items: center; }
  .menu-icon {
    position: absolute; left: 0; top: 0; width: 200px; height: 100%;
    display: flex; align-items: center; justify-content: center;
  }
  .menu-icon svg { fill: none; stroke: var(--icon-stroke); stroke-width: 3.5; stroke-linecap: round; stroke-linejoin: round; }
  .menu-label {
    position: absolute; left: 246px;
    font-family: "Source Sans 3", sans-serif; font-weight: 600;
    font-size: 53px; color: var(--label); letter-spacing: 0.2px;
  }

  .menu-toggle {
    position: absolute; left: 962px; top: 98px; width: 66px; height: 86px;
    background: var(--toggle-bg); box-shadow: 2px 3px 8px rgba(0,0,0,0.45);
  }
  .menu-toggle span { position: absolute; left: 16px; width: 36px; height: 7px; background: #fff; }
</style>
</head>
<body>
<div class="screen">
  <div class="status-bar"></div>

  <div class="content-strip">
    <div style="top:0;height:146px;background:var(--strip1)"></div>
    <div style="top:146px;height:244px;background:var(--strip2)"></div>
    <div style="top:390px;height:240px;background:var(--strip3)"></div>
    <div style="top:630px;height:238px;background:var(--strip4)"></div>
    <div style="top:868px;height:232px;background:var(--strip5)"></div>
    <div style="top:1100px;height:945px;background:linear-gradient(var(--strip6a),var(--strip6b))"></div>
  </div>

  <ul class="side-menu">
    <li class="menu-item" style="top:0;height:367px;background:var(--row1)">
      <div class="menu-icon" style="top:30px;height:337px;background:var(--row1-icon)">
        <svg width="144" height="104" viewBox="0 0 144 104">
          <path d="M30 78 C10 78 4 72 6 62 C8 52 20 48 26 46 C18 40 16 20 30 16 C44 14 46 34 40 44"/>
          <path d="M114 78 C134 78 140 72 138 62 C136 52 124 48 118 46 C126 40 128 20 114 16 C100 14 98 34 104 44"/>
          <path d="M72 94 C44 94 32 90 34 76 C36 64 50 58 58 56 C46 46 46 16 72 14 C98 16 98 46 86 56 C94 58 108 64 110 76 C112 90 100 94 72 94 Z"/>
        </svg>
      </div>
      <span class="menu-label" style="top:140px">My Groups</span>
    </li>
    <li class="menu-item" style="top:367px;height:338px;background:var(--row2)">
      <div class="menu-icon" style="background:var(--row2-icon)">
        <svg width="110" height="104" viewBox="0 0 110 104">
          <path d="M50 94 C20 94 6 92 8 78 C10 66 26 60 36 56 C22 46 22 10 50 8 C78 10 78 46 64 56 C70 58 76 60 80 64"/>
          <path d="M50 94 H90 C98 94 100 90 98 82"/>
          <path d="M86 44 V76 M70 60 H102"/>
        </svg>
      </div>
      <span class="menu-label" style="top:136px">Invite friends</span>
    </li>
    <li class="menu-item" style="top:705px;height:337px;background:var(--row3)">
      <div class="menu-icon" style="background:var(--row3-icon)">
        <svg width="56" height="48" viewBox="0 0 56 48">
          <path d="M6 4 V44 M19 14 V44 M32 22 V44 M46 18 V44"/>
        </svg>
      </div>
      <span class="menu-label" style="top:136px">Stats</span>
    </li>
    <li class="menu-item" style="top:1042px;height:338px;background:var(--row4)">
      <div class="menu-icon" style="background:var(--row4-icon)">
        <svg width="80" height="110" viewBox="0 0 80 110">
          <path d="M24 76 C24 62 6 54 6 38 C6 18 22 4 40 4 C58 4 74 18 74 38 C74 54 56 62 56 76 Z"/>
          <path d="M24 76 V96 C24 102 28 104 34 104 H46 C52 104 56 102 56 96 V76"/>
          <path d="M24 88 H56"/>
          <path d="M30 44 L40 56 L50 44 M40 56 V76"/>
        </svg>
      </div>
      <span class="menu-label" style="top:136px">Help</span>
    </li>
    <li class="menu-item" style="top:1380px;height:331px;background:var(--row5)">
      <div class="menu-icon" style="background:var(--row5-icon)">
        <svg width="84" height="80" viewBox="0 0 84 80" style="stroke:none;fill:var(--icon-stroke)">
          <rect x="18" y="2" width="48" height="20" rx="4"/>
          <path d="M10 24 H74 C80 24 84 28 84 34 V58 H68 V50 H16 V58 H0 V34 C0 28 4 24 10 24 Z"/>
          <rect x="70" y="32" width="6" height="6" rx="3" fill="var(--row5-icon)"/>
          <path d="M20 54 H64 V78 H20 Z"/>
          <rect x="26" y="60" width="32" height="3" fill="var(--row5-icon)"/>
          <rect x="26" y="67" width="32" height="3" fill="var(--row5-icon)"/>
        </svg>
      </div>
      <span class="menu-label" style="top:128px">Imprint</span>
    </li>
    <li class="menu-item" style="top:1711px;height:334px;background:var(--row6)">
      <div class="menu-icon" style="background:var(--row6-icon)">
        <svg width="72" height="80" viewBox="0 0 72 80">
          <path d="M24 18 C12 22 4 34 4 46 C4 64 18 76 36 76 C54 76 68 64 68 46 C68 34 60 22 48 18"/>
          <path d="M36 6 V48" stroke-width="6"/>
        </svg>
      </div>
      <span class="menu-label" style="top:128px">Signout</span>
    </li>
  </ul>

  <div class="menu-toggle" aria-label="Menu">
    <span style="top:14px"></span>
    <span style="top:31px"></span>
    <span style="top:48px"></span>
    <span style="top:65px"></span>
  </div>
</div>
</body>
</html>
```